Luxury artist needs high end & clean shopify website for selling prints

PLEASE REVIEW IN DETAIL DESIGN BRIEF IN UPLOADS
A luxury artist is in need of a high-end, clean, and aesthetically pleasing Shopify website to showcase and sell their unique prints. This website must reflect the upscale nature of the artist's work, with a focus on a polished, minimalist design that allows the art to take center stage.
The website should feature a user-friendly interface and seamless navigation to ensure a superior shopping experience for visitors. It should also include a secure and hassle-free checkout process, along with options for various payment methods.
In addition, the website should have features such as zoom-in capabilities to allow potential buyers to view the intricate details of each print, a section for customer reviews, and an about page detailing the artist's journey and inspiration.
Ultimately, this website will be more than just a sales platform; it will be an online gallery that represents the artist's brand, entices art enthusiasts, and facilitates the easy purchase of high-quality prints.
Target Market(s)
High end luxury art buyer
Look and feel
Each slider illustrates characteristics of the customer's brand and the style your logo design should communicate.

```html
<!DOCTYPE html>
<html lang="en">
<head>
<meta charset="utf-8">
<title>Verelle — Fine Art Prints</title>
<link rel="stylesheet" href="https://fonts.googleapis.com/css2?family=Playfair+Display:wght@400;500&family=Roboto:wght@300;400;500;700&display=swap">
<style>
:root{
  --accent:#bfa68c;
  --sand:#c6b6a3;
  --paper:#efefeb;
  --mist:#f6f6f8;
  --ink:#1e1e1e;
  --text:#3a3a3a;
  --footer:#0b0b0b;
  --white:#ffffff;
}
*{box-sizing:border-box;margin:0;padding:0}
html,body{width:1200px;height:5089px;overflow:hidden}
body{position:relative;font-family:'Roboto',sans-serif;color:var(--text);background:var(--white)}
.abs{position:absolute}
.serif{font-family:'Playfair Display',serif}
.btn{position:absolute;display:flex;align-items:center;justify-content:center;background:var(--accent);color:var(--white);font-size:15px;font-family:'Roboto',sans-serif}
.ph{position:absolute;overflow:hidden}
.section-title{position:absolute;left:0;width:1200px;text-align:center;font-family:'Playfair Display',serif;font-size:34px}
.section-title.gold{color:var(--accent)}

/* header + hero */
.hero{left:0;top:0;width:1200px;height:617px;
  background:
    radial-gradient(ellipse 420px 300px at 600px 330px,rgba(235,233,228,.55),rgba(235,233,228,0) 70%),
    radial-gradient(ellipse 260px 200px at 110px 420px,rgba(90,88,84,.35),rgba(90,88,84,0) 70%),
    radial-gradient(ellipse 300px 220px at 1080px 260px,rgba(95,92,88,.3),rgba(95,92,88,0) 70%),
    linear-gradient(180deg,#8f8d89 0%,#b4b2ad 30%,#bdbbb6 55%,#a19e98 80%,#7d838d 90%,#5f6774 100%)}
.topbar{left:0;top:0;width:1200px;height:91px;background:rgba(40,40,40,.92)}
.brand{position:absolute;font-family:'Roboto',sans-serif;font-weight:300;letter-spacing:8px;color:var(--white)}
.topbar .brand{left:104px;top:16px;font-size:44px;line-height:56px}
.nav{position:absolute;top:39px;color:var(--white);font-size:14px;font-weight:500}
.hero-card{left:281px;top:166px;width:638px;height:336px;background:#e6e5e3;box-shadow:0 6px 18px rgba(0,0,0,.25)}
.hero-card .brand{left:0;width:638px;text-align:center;top:50px;font-size:48px;line-height:56px;color:var(--ink)}
.hero-card h1{position:absolute;left:0;width:638px;text-align:center;top:158px;font-family:'Playfair Display',serif;font-weight:400;font-size:31px;color:var(--ink)}

/* about */
.band-paper{left:0;top:617px;width:1200px;height:1722px;background:var(--paper)}
.about-text{left:678px;top:782px;font-size:14px;line-height:33.4px;color:var(--text);white-space:nowrap}
.tab{position:absolute;top:1307px;height:53px;display:flex;align-items:center;justify-content:center;font-size:17px;font-weight:500}
.arrow{position:absolute;width:50px;height:50px;border-radius:50%;background:var(--accent);display:flex;align-items:center;justify-content:center}

/* reviews */
.review-text{left:111px;top:2024px;font-size:14.5px;line-height:33.5px;white-space:nowrap}
.reviewer{left:111px;top:2164px;font-size:21px;font-weight:500;color:var(--accent)}
.dot{position:absolute;top:2225px;width:13px;height:13px;border-radius:50%;border:1.5px solid var(--accent)}

/* contact */
.band-mist{left:0;top:2339px;width:1200px;height:593px;background:linear-gradient(120deg,#ffffff 0%,var(--mist) 60%,#eeeef1 100%)}
.field{position:absolute;height:65px;background:var(--white);border:1px solid #d9d9d9;padding:24px 26px;font-size:14px;font-weight:500;color:var(--ink)}

/* products */
.products-text{left:109px;top:3212px;font-size:14px;line-height:33.5px;color:var(--ink);white-space:nowrap}
.card{position:absolute;top:3029px;width:317px;height:447px;background:var(--white);box-shadow:0 2px 10px rgba(0,0,0,.12)}
.card h3{position:absolute;left:0;width:100%;top:308px;text-align:center;font-family:'Playfair Display',serif;font-weight:400;font-size:22px;color:var(--ink)}
.cart{position:absolute;right:12px;top:18px;width:50px;height:50px;border-radius:50%;background:rgba(191,166,140,.85);display:flex;align-items:center;justify-content:center}

/* newsletter */
.band-sand{left:0;top:3575px;width:1200px;height:349px;background:var(--sand)}
.news-text{left:0;top:3697px;width:1200px;text-align:center;font-size:14.5px;line-height:33.5px;color:#5a4f44}

/* blog */
.blog-date{position:absolute;top:4412px;font-size:17px;font-weight:500;color:#a9a9a9}
.blog-text{position:absolute;top:4458px;font-size:14px;line-height:33.5px;white-space:nowrap}

/* footer */
.footer{left:0;top:4717px;width:1200px;height:372px;background:var(--footer);color:var(--white)}
.footer h4{position:absolute;font-family:'Playfair Display',serif;font-weight:400;font-size:21px}
.flink{position:absolute;left:500px;font-size:14px}
.chev{position:absolute;left:453px;font-size:12px}
.cinfo{position:absolute;left:837px;font-size:14px}
.ic{position:absolute;left:791px;width:30px;height:30px;border-radius:50%;background:#2a2a2a;display:flex;align-items:center;justify-content:center}
</style>
</head>
<body>

<!-- Hero -->
<div class="abs hero" role="img" aria-label="Gallery wall of textured concrete with hanging pendant bulbs above a sofa"></div>
<header class="abs topbar">
  <div class="brand">VERELLE</div>
  <span class="nav" style="left:354px">HOME</span>
  <span class="nav" style="left:431px">ORIGINAL ARTWORK</span>
  <span class="nav" style="left:605px">REPRODUCTIONS</span>
  <span class="nav" style="left:757px">EVENTS/EXHIBITIONS</span>
  <span class="nav" style="left:941px">THE ARTIST/CONTACT</span>
</header>
<div class="abs hero-card">
  <div class="brand">VERELLE</div>
  <h1>Welcome to Verelle</h1>
  <div class="btn" style="left:237px;top:237px;width:164px;height:42px">Get Started</div>
</div>

<!-- About + Gallery + Reviews -->
<div class="abs band-paper"></div>
<div class="ph" style="left:330px;top:714px;width:277px;height:367px;border-radius:14px;background:
  radial-gradient(ellipse 110px 80px at 170px 110px,rgba(246,205,190,.9),rgba(246,205,190,0) 75%),
  radial-gradient(ellipse 120px 90px at 200px 230px,rgba(232,168,150,.85),rgba(232,168,150,0) 75%),
  linear-gradient(165deg,#d9d0c8 0%,#e8b3a2 30%,#d88f7d 55%,#9e6e5a 80%,#4a3a30 100%)" role="img" aria-label="Photo of a baby's feet"></div>
<div class="ph" style="left:111px;top:762px;width:278px;height:369px;border-radius:14px;box-shadow:0 2px 8px rgba(0,0,0,.15);background:
  radial-gradient(ellipse 100px 110px at 150px 120px,rgba(178,120,88,.95),rgba(178,120,88,0) 75%),
  radial-gradient(ellipse 70px 60px at 70px 230px,rgba(206,62,60,.55),rgba(206,62,60,0) 80%),
  radial-gradient(ellipse 90px 70px at 220px 200px,rgba(60,80,170,.45),rgba(60,80,170,0) 80%),
  radial-gradient(ellipse 160px 100px at 110px 330px,rgba(40,120,50,.9),rgba(40,120,50,0) 80%),
  linear-gradient(180deg,#6b4a38 0%,#9a7058 45%,#b6a296 75%,#8a8f86 100%)" role="img" aria-label="Photo of a child with paint on the face and hands"></div>
<div class="abs serif" style="left:678px;top:718px;font-size:31px;color:var(--accent)">About Us</div>
<p class="abs about-text">Sed ut perspiciatis unde omnis iste natus error sit<br>voluptatem accusantium doloremque laudantium, totam<br>rem aperiam, eaque ipsa quae ab illo inve<br>ntore veritatis et quasi architecto beatae vitae dicta sunt<br>explicabo. Nemo enim ipsam voluptatem quia voluptas sit<br>aspernatur aut odit aut fugit, sed quia consequuntur magni<br>dolores eos qui ratione voluptatem sequi nesciunt. Neque</p>
<div class="btn" style="left:678px;top:1052px;width:165px;height:42px">Learn More</div>

<div class="section-title" style="top:1218px;color:var(--ink)">Our Gallery</div>
<div class="tab" style="left:366px;width:225px;background:var(--accent);color:var(--white)">The Marlow Gallery</div>
<div class="tab" style="left:607px;width:225px;background:var(--white);border:2px solid #9c9c9c;color:var(--ink)">Northlight Gallery</div>

<div class="ph" style="left:111px;top:1421px;width:308px;height:307px;background:
  radial-gradient(ellipse 130px 90px at 150px 140px,rgba(236,226,200,.75),rgba(236,226,200,0) 75%),
  linear-gradient(90deg,rgba(20,20,22,.6) 0%,rgba(20,20,22,0) 20%,rgba(20,20,22,0) 80%,rgba(20,20,22,.6) 100%),
  linear-gradient(180deg,#1f2124 0%,#4b4a45 25%,#a69c85 50%,#5e564a 68%,#2e2520 82%,#4a3626 100%)" role="img" aria-label="Visitors inside a lit gallery seen through glass"></div>
<div class="ph" style="left:445px;top:1421px;width:308px;height:307px;background:
  radial-gradient(ellipse 150px 120px at 170px 110px,rgba(238,238,236,.9),rgba(238,238,236,0) 75%),
  radial-gradient(ellipse 110px 80px at 200px 250px,rgba(40,40,42,.75),rgba(40,40,42,0) 75%),
  radial-gradient(ellipse 40px 120px at 20px 120px,rgba(30,30,30,.6),rgba(30,30,30,0) 80%),
  linear-gradient(180deg,#c8c8c6 0%,#d8d8d6 45%,#9a9a98 75%,#6e6e6c 100%)" role="img" aria-label="Visitors viewing black figure drawings on a white wall"></div>
<div class="ph" style="left:781px;top:1421px;width:306px;height:307px;background:
  radial-gradient(ellipse 120px 140px at 150px 150px,rgba(230,205,150,.75),rgba(230,205,150,0) 75%),
  radial-gradient(ellipse 70px 110px at 150px 150px,rgba(25,22,20,.8),rgba(25,22,20,0) 80%),
  radial-gradient(ellipse 60px 30px at 150px 275px,rgba(240,238,232,.8),rgba(240,238,232,0) 80%),
  linear-gradient(180deg,#5e6068 0%,#7a7870 45%,#6a655c 75%,#4c4842 100%)" role="img" aria-label="Black figure sculpture displayed on a plinth under warm light"></div>
<div class="arrow" style="left:26px;top:1551px"><svg width="24" height="14" viewBox="0 0 24 14"><path d="M23 7H2M8 1L2 7l6 6" fill="none" stroke="#fff" stroke-width="1.8"/></svg></div>
<div class="arrow" style="left:1112px;top:1551px"><svg width="24" height="14" viewBox="0 0 24 14"><path d="M1 7h21M16 1l6 6-6 6" fill="none" stroke="#fff" stroke-width="1.8"/></svg></div>

<div class="section-title gold" style="top:1816px">Customer Reviews</div>
<div class="ph" style="left:112px;top:1903px;width:100px;height:100px;border-radius:50%;background:
  radial-gradient(circle at 50px 30px,rgba(170,110,80,.85),rgba(170,110,80,0) 45%),
  linear-gradient(180deg,#ececec 0%,#e8e2dc 40%,#e98a55 65%,#dd6a32 100%)" role="img" aria-label="Reviewer portrait"></div>
<p class="abs review-text">Sed ut perspiciatis unde omnis iste natus error sit voluptatem<br>accusantium doloremque laudantium, totam rem aperiam,<br>eaque ipsa quae ab illo inventore veritatis et quasi architecto<br>beatae vitae dicta sunt explicabo.</p>
<div class="abs reviewer">Lorem ipsum</div>
<span class="dot" style="left:112px;background:var(--accent)"></span>
<span class="dot" style="left:137px"></span>
<span class="dot" style="left:163px"></span>
<div class="ph" style="left:599px;top:1898px;width:488px;height:340px;border-radius:6px;background:
  radial-gradient(ellipse 200px 40px at 210px 90px,rgba(40,40,40,.55),rgba(40,40,40,0) 80%),
  radial-gradient(ellipse 120px 70px at 250px 290px,rgba(250,250,250,.95),rgba(250,250,250,0) 80%),
  radial-gradient(ellipse 80px 60px at 450px 130px,rgba(120,120,120,.5),rgba(120,120,120,0) 80%),
  linear-gradient(180deg,#9c9c9c 0%,#d6d6d6 25%,#ececec 55%,#bdbdbd 85%,#a8a8a8 100%)" role="img" aria-label="White gallery interior with framed figure drawings and sculpture"></div>

<!-- Contact -->
<div class="abs band-mist"></div>
<div class="section-title gold" style="top:2392px">Contact Us</div>
<div class="field" style="left:168px;top:2495px;width:417px">Your First Name</div>
<div class="field" style="left:615px;top:2495px;width:416px">Your Last Name</div>
<div class="field" style="left:168px;top:2590px;width:417px">Your Email Address</div>
<div class="field" style="left:615px;top:2590px;width:416px">Your Phone Number</div>
<div class="field" style="left:168px;top:2685px;width:863px;height:97px">Your Message Here</div>
<div class="btn" style="left:518px;top:2823px;width:164px;height:44px">Submit Now</div>

<!-- Products -->
<div class="abs serif" style="left:109px;top:3145px;font-size:32px;color:var(--accent)">Our Products</div>
<p class="abs products-text">Limited Edition Prints are printed in small<br>quantities and once that print run is complete<br>no more are made.&nbsp; Each print is numbered<br>and comes with a signed Certificate of<br>Authenticity.</p>
<div class="card" style="left:474px">
  <div class="ph" style="left:9px;top:9px;width:299px;height:262px;background:
    radial-gradient(ellipse 90px 100px at 150px 100px,rgba(250,250,250,.95),rgba(250,250,250,0) 75%),
    radial-gradient(ellipse 120px 120px at 150px 110px,rgba(30,30,30,.45),rgba(30,30,30,0) 80%),
    radial-gradient(ellipse 140px 40px at 150px 230px,rgba(60,60,60,.5),rgba(60,60,60,0) 80%),
    linear-gradient(180deg,#e6e6e6 0%,#f0f0f0 50%,#cfcfcf 85%,#b0b0b0 100%)" role="img" aria-label="Framed black figure painting with white ceramic objects"></div>
  <div class="cart"><svg width="24" height="22" viewBox="0 0 24 22"><path d="M1 2h4l3 12h11l3-9H7" fill="none" stroke="#fff" stroke-width="1.6"/><circle cx="10" cy="18" r="1.6" fill="#fff"/><circle cx="17" cy="18" r="1.6" fill="#fff"/></svg></div>
  <h3>Original Paintings</h3>
  <div class="btn" style="left:95px;top:366px;width:128px;height:43px">Buy Now</div>
</div>
<div class="card" style="left:801px">
  <div class="ph" style="left:8px;top:9px;width:299px;height:262px;background:
    radial-gradient(ellipse 60px 140px at 20px 120px,rgba(120,78,50,.85),rgba(120,78,50,0) 80%),
    radial-gradient(ellipse 110px 90px at 180px 150px,rgba(245,244,240,.95),rgba(245,244,240,0) 80%),
    radial-gradient(ellipse 140px 40px at 170px 245px,rgba(40,40,40,.55),rgba(40,40,40,0) 80%),
    linear-gradient(180deg,#a07a5c 0%,#e4e1db 30%,#d2cfc9 70%,#8c8984 100%)" role="img" aria-label="Printed catalogue booklets showing a gallery interior"></div>
  <div class="cart"><svg width="24" height="22" viewBox="0 0 24 22"><path d="M1 2h4l3 12h11l3-9H7" fill="none" stroke="#fff" stroke-width="1.6"/><circle cx="10" cy="18" r="1.6" fill="#fff"/><circle cx="17" cy="18" r="1.6" fill="#fff"/></svg></div>
  <h3>Merch | Objects</h3>
  <div class="btn" style="left:95px;top:366px;width:128px;height:43px">Buy Now</div>
</div>
<div class="arrow" style="left:1128px;top:3233px;width:38px;height:38px"><svg width="20" height="12" viewBox="0 0 20 12"><path d="M1 6h17M13 1l5 5-5 5" fill="none" stroke="#fff" stroke-width="1.6"/></svg></div>

<!-- Newsletter -->
<div class="abs band-sand"></div>
<div class="section-title" style="top:3628px;color:var(--ink)">Subscribe To Our Newsletter</div>
<p class="abs news-text">Sed ut perspiciatis unde omnis iste natus error sit voluptatem accusantium doloremque laudantium, totam<br>rem aperiam, eaque ipsa quae ab illo inventore veritatis et</p>
<div class="abs" style="left:376px;top:3806px;width:274px;height:51px;background:var(--white);padding:17px 20px;font-size:14px;color:var(--ink)">Enter Email Address</div>
<div class="abs" style="left:650px;top:3806px;width:172px;height:51px;background:#3a3a3a;color:var(--white);display:flex;align-items:center;justify-content:center;font-size:17px;font-weight:500">Subscribe Now</div>

<!-- Blogs -->
<div class="section-title gold" style="top:4013px">Latest Blogs</div>
<div class="ph" style="left:111px;top:4144px;width:316px;height:221px;background:
  radial-gradient(ellipse 180px 40px at 158px 30px,rgba(240,240,242,.9),rgba(240,240,242,0) 80%),
  radial-gradient(ellipse 70px 80px at 60px 150px,rgba(25,25,25,.7),rgba(25,25,25,0) 80%),
  radial-gradient(ellipse 90px 80px at 240px 150px,rgba(235,235,235,.8),rgba(235,235,235,0) 80%),
  linear-gradient(180deg,#c7cbcf 0%,#8f9296 30%,#a9a9a9 60%,#3c3c3c 100%)" role="img" aria-label="Outdoor art fair tent with hanging framed prints"></div>
<div class="ph" style="left:441px;top:4144px;width:316px;height:221px;background:
  radial-gradient(ellipse 150px 60px at 158px 60px,rgba(248,248,250,.95),rgba(248,248,250,0) 80%),
  radial-gradient(ellipse 90px 60px at 90px 170px,rgba(20,20,24,.7),rgba(20,20,24,0) 80%),
  radial-gradient(ellipse 60px 60px at 260px 160px,rgba(210,220,235,.8),rgba(210,220,235,0) 80%),
  linear-gradient(180deg,#3f77c2 0%,#79a3d6 25%,#c9d3dc 50%,#6d7a5e 80%,#3f5534 100%)" role="img" aria-label="White canopy booth displaying artwork outdoors"></div>
<div class="ph" style="left:771px;top:4144px;width:316px;height:221px;background:
  radial-gradient(ellipse 80px 70px at 90px 60px,rgba(250,250,250,.9),rgba(250,250,250,0) 80%),
  radial-gradient(ellipse 80px 70px at 170px 140px,rgba(20,20,20,.85),rgba(20,20,20,0) 80%),
  radial-gradient(ellipse 60px 60px at 280px 130px,rgba(25,25,25,.7),rgba(25,25,25,0) 80%),
  linear-gradient(160deg,#ececec 0%,#d2d2d2 40%,#8e8e8e 70%,#d8d8d8 100%)" role="img" aria-label="Framed black and white figure prints"></div>
<div class="blog-date" style="left:111px">23RD JUNE 2023</div>
<div class="blog-date" style="left:441px">06TH APRIL 2023</div>
<div class="blog-date" style="left:771px">9TH AUGUST 2023</div>
<p class="blog-text" style="left:111px">Sed ut perspiciatis unde omnis iste natus<br>error sit voluptatem accusantium<br>doloremque laudantium, totam rem</p>
<p class="blog-text" style="left:441px">Sed ut perspiciatis unde omnis iste natus<br>error sit voluptatem accusantium<br>doloremque laudantium, totam rem</p>
<p class="blog-text" style="left:771px">Sed ut perspiciatis unde omnis iste natus<br>error sit voluptatem accusantium<br>doloremque laudantium, totam rem</p>
<div class="btn" style="left:111px;top:4581px;width:129px;height:41px">Read More</div>
<div class="btn" style="left:441px;top:4581px;width:129px;height:41px">Read More</div>
<div class="btn" style="left:771px;top:4581px;width:129px;height:41px">Read More</div>

<!-- Footer -->
<footer class="abs footer">
  <div class="brand" style="left:128px;top:110px;font-size:46px;line-height:56px">VERELLE</div>
  <span class="abs" style="left:178px;top:218px;width:36px;height:36px;border-radius:50%;background:#2a2a2a"></span>
  <span class="abs" style="left:233px;top:218px;width:36px;height:36px;border-radius:50%;background:#2a2a2a;display:flex;align-items:center;justify-content:center"><svg width="16" height="12" viewBox="0 0 16 12"><rect x=".8" y=".8" width="14.4" height="10.4" fill="none" stroke="#fff" stroke-width="1.4"/><path d="M1 1l7 6 7-6" fill="none" stroke="#fff" stroke-width="1.4"/></svg></span>

  <h4 style="left:453px;top:70px">Quick Links</h4>
  <span class="chev" style="top:132px">›</span><span class="flink" style="top:131px">Home</span>
  <span class="chev" style="top:168px">›</span><span class="flink" style="top:167px">Original Artwork</span>
  <span class="chev" style="top:204px">›</span><span class="flink" style="top:203px">Reproductions</span>
  <span class="chev" style="top:240px">›</span><span class="flink" style="top:239px">Events/Exhibitions</span>
  <span class="chev" style="top:276px">›</span><span class="flink" style="top:275px">The Artist/Contact</span>

  <h4 style="left:791px;top:70px">Contact Us</h4>
  <span class="ic" style="top:124px"><svg width="12" height="12" viewBox="0 0 12 12"><path d="M2 1l2 0 1 3-1.5 1a7 7 0 0 0 3.5 3.5L8 7l3 1v2a1 1 0 0 1-1 1A9 9 0 0 1 1 2a1 1 0 0 1 1-1z" fill="#fff"/></svg></span>
  <span class="cinfo" style="top:130px">+1 555 014 2290</span>
  <span class="ic" style="top:168px"><svg width="12" height="9" viewBox="0 0 12 9"><rect width="12" height="9" fill="#fff"/><path d="M0 0l6 5 6-5" fill="none" stroke="#2a2a2a" stroke-width="1.2"/></svg></span>
  <span class="cinfo" style="top:174px">studio@verelle.com</span>
  <span class="ic" style="top:212px"><svg width="10" height="13" viewBox="0 0 10 13"><path d="M5 13S0 7.5 0 5a5 5 0 0 1 10 0c0 2.5-5 8-5 8z" fill="#fff"/><circle cx="5" cy="5" r="1.8" fill="#2a2a2a"/></svg></span>
  <span class="cinfo" style="top:218px">42/3, Fairhaven, Maple County,</span>
  <span class="cinfo" style="top:262px">lorem lipsum, 514 207</span>

  <div class="abs" style="left:128px;top:305px;width:944px;height:1px;background:#3a3a3a"></div>
  <span class="abs" style="left:128px;top:337px;font-size:12px;font-weight:500">@2023 COPYRIGHTS. VERELLE. ALL RIGHTS RESERVED.</span>
  <span class="abs" style="left:1042px;top:330px;width:30px;height:30px;border-radius:50%;background:var(--white)"></span>
</footer>

</body>
</html>
```